new business card design - modern, professional, bold, B2B focus - with QR code pls

we are looking for a modern looking, colorful, business card design. some highlights:
- put space for QR code please. probably on the back but I'm open.
- biz card to be orientated VERTICAL not the traditional horizontal.
- do NOT use our full name on the card (ie: Allied Furnace Servicing Inc). Use only AFS Inc or AFS.
- use black and orange with some white. ideally black card with orange and white for the letters/logo etc. gray ok too - for outlines etc.
- we work in HEAVY industrial, so the cards should lend itself to this. our website is alfurnace.example, so you can see what we do.
- do NOT put in little smoke stack pictures / silouettes etc.
- think MODERN and INDUSTRIAL, with a techy focus.

Industry/Entity Type

heavy industrial - all of them. we perform maintenance and inspection services at heavy industrial and commercial businesses. so B2B

Contact Information for Business Card

name, title, phone numbers (cell + hardline), website, email address. of course our logo too - either on front or front and back.

Font styles to use
Other font styles liked:
• montserrat

Colors
F0912C
F2A743
F7CA91
FBE8D2
FDF5EE

Requirements
Must have
• see description
Nice to have
• see description
Should not have
• see description

```html
<!DOCTYPE html>
<html lang="en">
<head>
<meta charset="utf-8">
<title>AFS Inc — Business Card</title>
<link rel="stylesheet" href="https://fonts.googleapis.com/css2?family=Montserrat:wght@400;500;800&family=Oswald:wght@700&display=swap">
<style>
  :root {
    --backdrop: #1a1a1b;
    --card: #2b2b2d;
    --orange: #f39a0a;
    --white: #ffffff;
    --grey: #8a8a8d;
    --faint: #3a3a3c;
    --shadow: rgba(0,0,0,0.55);
  }
  html, body {
    margin: 0;
    padding: 0;
    width: 1200px;
    height: 1200px;
    overflow: hidden;
    background: var(--backdrop);
  }
  .canvas {
    position: relative;
    width: 1200px;
    height: 1200px;
  }
  .card {
    position: absolute;
    top: 240px;
    width: 440px;
    height: 720px;
    background: var(--card);
    border-radius: 28px;
    box-shadow: 0 18px 40px var(--shadow);
    overflow: hidden;
    font-family: "Montserrat", sans-serif;
    color: var(--white);
    text-align: center;
  }
  .card--front { left: 100px; }
  .card--back { left: 660px; }

  .front-mark {
    margin: 90px 0 0;
    font-weight: 800;
    font-size: 150px;
    letter-spacing: -4px;
    line-height: 1;
    color: var(--faint);
  }
  .person-name {
    margin: 70px 0 0;
    font-family: "Oswald", sans-serif;
    font-weight: 700;
    font-size: 34px;
    letter-spacing: 1px;
    color: var(--orange);
    line-height: 1;
  }
  .person-title {
    margin: 8px 0 0;
    font-size: 21px;
    font-weight: 400;
  }
  .icon-row {
    display: flex;
    align-items: center;
    justify-content: center;
    gap: 8px;
    margin: 22px 0 0;
  }
  .icon-row .rule {
    width: 80px;
    height: 1.5px;
    background: var(--orange);
  }
  .icon-row .rule--left { margin-right: 10px; }
  .icon-row .rule--right { margin-left: 10px; }
  .contact-icon {
    width: 22px;
    height: 22px;
    background: var(--orange);
    border-radius: 4px;
    display: flex;
    align-items: center;
    justify-content: center;
  }
  .contact-list {
    margin: 14px 0 0;
    padding: 0;
    list-style: none;
    font-size: 19px;
    font-weight: 500;
    line-height: 1.38;
  }
  .address-rule {
    width: 300px;
    height: 1.5px;
    background: var(--orange);
    margin: 18px auto 14px;
  }
  .address {
    font-style: normal;
    font-size: 18px;
    font-weight: 500;
    line-height: 1.4;
  }

  .back-mark {
    position: absolute;
    left: 0;
    right: 0;
    top: 190px;
    font-weight: 800;
    font-size: 150px;
    letter-spacing: -4px;
    line-height: 1;
    color: var(--orange);
  }
  .qr-space {
    position: absolute;
    left: 50%;
    top: 450px;
    width: 150px;
    height: 150px;
    margin-left: -75px;
    box-sizing: border-box;
    border: 2px dashed var(--grey);
    border-radius: 10px;
  }
</style>
</head>
<body>
<main class="canvas">
  <section class="card card--front" aria-label="Card front">
    <div class="front-mark">AFS</div>
    <h1 class="person-name">DANIEL CARTER</h1>
    <p class="person-title">CEO/Founder</p>
    <div class="icon-row">
      <span class="rule rule--left"></span>
      <span class="contact-icon" aria-label="Phone">
        <svg width="14" height="14" viewBox="0 0 24 24"><path fill="#2b2b2d" d="M6.6 10.8a15 15 0 0 0 6.6 6.6l2.2-2.2c.3-.3.7-.4 1-.2 1.1.4 2.300.6 3.600.6.6 0 1 .4 1 1V20c0 .6-.4 1-1 1A17 17 0 0 1 3 4c0-.6.4-1 1-1h3.5c.6 0 1 .4 1 1 0 1.3.2 2.5.6 3.6.1.3 0 .7-.2 1z"/></svg>
      </span>
      <span class="contact-icon" aria-label="Mobile">
        <svg width="14" height="14" viewBox="0 0 24 24"><rect x="6" y="2" width="12" height="20" rx="2" fill="none" stroke="#2b2b2d" stroke-width="2.4"/><circle cx="12" cy="18" r="1.3" fill="#2b2b2d"/></svg>
      </span>
      <span class="contact-icon" aria-label="Email">
        <svg width="14" height="14" viewBox="0 0 24 24"><rect x="2" y="5" width="20" height="14" rx="1.5" fill="#2b2b2d"/><path d="M3 6l9 7 9-7" fill="none" stroke="#f39a0a" stroke-width="1.8"/></svg>
      </span>
      <span class="contact-icon" aria-label="Website">
        <svg width="14" height="14" viewBox="0 0 24 24"><circle cx="12" cy="12" r="9" fill="none" stroke="#2b2b2d" stroke-width="2.2"/><path d="M3 12h18M12 3c3 3 3 15 0 18M12 3c-3 3-3 15 0 18" fill="none" stroke="#2b2b2d" stroke-width="1.6"/></svg>
      </span>
      <span class="rule rule--right"></span>
    </div>
    <ul class="contact-list">
      <li>877-FURNACE</li>
      <li>905-555-0142</li>
      <li>afsinc@alfurnace.example</li>
      <li>www.alfurnace.example</li>
    </ul>
    <div class="address-rule"></div>
    <address class="address">1420 Foundry Lane, Unit #2.<br>Milton, On L9T 0A1, Canada</address>
  </section>

  <section class="card card--back" aria-label="Card back">
    <div class="back-mark">AFS</div>
    <div class="qr-space" role="img" aria-label="Reserved space for QR code"></div>
  </section>
</main>
</body>
</html>
```